Design a beautiful book cover for my self help book

The Craft of Hush is a book I've written about how I learnt to quite my mind, rid myself of old pain and stand in my intuition. It's one simple practical tool to find you moment and step into your abundance. We need a cover that reflects this amazing concept! The current cover is attached. It's too dark and not in tune with the market. Please search books with similar content and make design similar yet different.

Target Market(s)

People into self help or motivational content. As well as people suffering from depression, stress, anxiety etc.

Industry/Entity Type

Self Help

Requirements
Must have
• A light airy feel of freedom
Nice to have
• Some sort of linage from current cover
Should not have
• Dark, ambiguous,

```html
<!DOCTYPE html>
<html lang="en">
<head>
<meta charset="utf-8">
<title>The Craft of Hush — Book Cover</title>
<link rel="stylesheet" href="https://fonts.googleapis.com/css2?family=Raleway:wght@300&family=Oswald:wght@600&family=Montserrat:wght@800&display=swap">
<style>
  :root {
    --sky: #5bcbf5;
    --sky-light: #bfe9fb;
    --glow: #ffffff;
    --sun: #f7d51a;
    --band: #ffffff;
    --page: #ffffff;
    --author: #ffffff;
  }
  * { margin: 0; padding: 0; box-sizing: border-box; }
  html, body {
    width: 1200px;
    height: 1200px;
    overflow: hidden;
    background: var(--page);
  }
  .canvas {
    position: relative;
    width: 1200px;
    height: 1200px;
  }
  .cover {
    position: absolute;
    left: 250px;
    top: 75px;
    width: 700px;
    height: 1050px;
    overflow: hidden;
    background: radial-gradient(circle at 50% 50%, var(--glow) 0%, var(--sky-light) 22%, var(--sky) 52%, var(--sky) 100%);
  }
  .cover__burst {
    position: absolute;
    left: 60px;
    top: 236px;
    width: 580px;
    height: 580px;
  }
  .cover__band {
    position: absolute;
    left: 0;
    top: 385px;
    width: 100%;
    height: 47px;
    background: var(--band);
  }
  .cover__kicker {
    position: absolute;
    left: 0;
    top: 381px;
    width: 100%;
    text-align: center;
    font-family: "Raleway", sans-serif;
    font-weight: 300;
    font-size: 46px;
    line-height: 1;
    letter-spacing: 1px;
    color: var(--sun);
    text-transform: uppercase;
  }
  .cover__title {
    position: absolute;
    left: 0;
    top: 430px;
    width: 100%;
    text-align: center;
    font-family: "Oswald", sans-serif;
    font-weight: 600;
    font-size: 170px;
    line-height: 1;
    letter-spacing: -2px;
    color: var(--sun);
    transform: skewX(-10deg);
  }
  .cover__author {
    position: absolute;
    left: 0;
    top: 978px;
    width: 100%;
    text-align: center;
    font-family: "Montserrat", sans-serif;
    font-weight: 800;
    font-size: 34px;
    line-height: 1;
    letter-spacing: 1px;
    color: var(--author);
    text-transform: uppercase;
  }
</style>
</head>
<body>
  <div class="canvas">
    <div class="cover">
      <svg class="cover__burst" viewBox="0 0 580 580" role="img" aria-label="Soft sunburst of fine white and yellow rays radiating from the title">
        <defs>
          <radialGradient id="burstGlow" cx="50%" cy="50%" r="50%">
            <stop offset="0%" stop-color="#ffffff" stop-opacity="0.9"/>
            <stop offset="45%" stop-color="#fff6c4" stop-opacity="0.35"/>
            <stop offset="100%" stop-color="#fff6c4" stop-opacity="0"/>
          </radialGradient>
        </defs>
        <circle cx="290" cy="290" r="290" fill="url(#burstGlow)"/>
      </svg>
      <div class="cover__band"></div>
      <h1 class="cover__kicker">The Craft of</h1>
      <div class="cover__title">Hush</div>
      <p class="cover__author">Corey Lund</p>
    </div>
  </div>
</body>
</html>
```